Marrowby Lane School bookmark

We need a vertical card (DL 99x210 mm) that will be put inside books at a primary school for children to make comments about the books. Text at the top:
Marrowby Lane School (and logo)
What did you think of this book?

Text at the bottom:
Pass it on!

Words in repeated pattern around the edge: funny sad exciting mysterious fantastic boring enthralling interesting

It should be in interesting bright colours with a white or pale background as children will write on the cards

The card should be double sided with the same design on each side

Industry/Entity Type

School

```html
<!DOCTYPE html>
<html lang="en">
<head>
<meta charset="utf-8">
<title>Marrowby Lane School bookmark</title>
<link rel="stylesheet" href="https://fonts.googleapis.com/css2?family=Itim&family=Tinos:wght@700&family=Arimo:wght@700&display=swap">
<style>
  :root {
    --border-red: #c8202f;
    --school-red: #c41e2a;
    --star-yellow: #ffd21f;
    --orange: #f5821f;
    --paper: #ffffff;
    --frame-gold: #b8963a;
    --rule-grey: #d2d2d2;
    --logo-dark: #8e1a1f;
    --kids-tone: #e9eef5;
  }
  html, body {
    margin: 0;
    padding: 0;
    width: 1200px;
    height: 900px;
    overflow: hidden;
    background: var(--paper);
  }
  .sheet {
    position: relative;
    width: 1200px;
    height: 900px;
  }
  .bookmark {
    position: absolute;
    top: 5px;
    width: 412px;
    height: 873px;
    background: var(--border-red);
  }
  .bookmark--front { left: 190px; }
  .bookmark--back { left: 629px; }

  .border-words {
    position: absolute;
    inset: 0;
    width: 412px;
    height: 873px;
    font-family: "Itim", "Comic Sans MS", cursive;
    font-size: 15px;
  }
  .border-words .word { fill: #ffffff; }
  .border-words .star { fill: var(--star-yellow); font-size: 11px; }

  .panel {
    position: absolute;
    left: 20px;
    top: 20px;
    width: 370px;
    height: 831px;
    background: var(--paper);
    border: 1px solid var(--frame-gold);
  }
  .school-mark {
    position: absolute;
    left: 5px;
    top: 12px;
    width: 48px;
    height: 48px;
    border-radius: 50%;
    background: var(--logo-dark);
    border: 2px solid #222;
    box-sizing: border-box;
  }
  .school-name {
    position: absolute;
    left: 63px;
    top: 18px;
    margin: 0;
    font-family: "Tinos", "Times New Roman", serif;
    font-weight: 700;
    font-size: 28px;
    line-height: 36px;
    color: var(--school-red);
    white-space: nowrap;
  }
  .kids-art {
    position: absolute;
    left: 272px;
    top: 55px;
    width: 84px;
    height: 52px;
    background: linear-gradient(90deg, var(--kids-tone), #f7e7ef);
    border-radius: 22px 22px 0 0;
  }
  .prompt {
    position: absolute;
    left: 25px;
    top: 102px;
    width: 321px;
    height: 80px;
    margin: 0;
    border-radius: 12px;
    background: var(--orange);
    color: #ffffff;
    font-family: "Itim", "Comic Sans MS", cursive;
    font-weight: 400;
    font-size: 28px;
    line-height: 40px;
    text-align: center;
    padding-top: 1px;
    box-sizing: border-box;
  }
  .writing-lines {
    position: absolute;
    left: 10px;
    top: 232px;
    width: 350px;
    margin: 0;
    padding: 0;
    list-style: none;
  }
  .writing-lines li {
    height: 36.7px;
    border-top: 1px solid var(--rule-grey);
    box-sizing: border-box;
  }
  .pass-on {
    position: absolute;
    left: 87px;
    top: 751px;
    width: 196px;
    height: 40px;
    margin: 0;
    background: var(--orange);
    color: #ffffff;
    font-family: "Arimo", Arial, sans-serif;
    font-weight: 700;
    font-size: 28px;
    line-height: 40px;
    text-align: center;
  }
</style>
</head>
<body>
<main class="sheet">

  <article class="bookmark bookmark--front">
    <svg class="border-words" viewBox="0 0 412 873" aria-hidden="true">
      <text x="40" y="16" textLength="365" lengthAdjust="spacingAndGlyphs"><tspan class="word">Funny </tspan><tspan class="star">★</tspan><tspan class="word"> Sad </tspan><tspan class="star">★</tspan><tspan class="word"> Exciting </tspan><tspan class="star">★</tspan><tspan class="word"> Mysterious </tspan><tspan class="star">★</tspan><tspan class="word"> Fantastic</tspan></text>
      <text transform="translate(398,40) rotate(90)" textLength="805" lengthAdjust="spacingAndGlyphs"><tspan class="word">Funny </tspan><tspan class="star">★</tspan><tspan class="word"> Sad </tspan><tspan class="star">★</tspan><tspan class="word"> Exciting </tspan><tspan class="star">★</tspan><tspan class="word"> Mysterious </tspan><tspan class="star">★</tspan><tspan class="word"> Fantastic </tspan><tspan class="star">★</tspan><tspan class="word"> Boring </tspan><tspan class="star">★</tspan><tspan class="word"> Enthralling </tspan><tspan class="star">★</tspan><tspan class="word"> Interesting </tspan><tspan class="star">★</tspan><tspan class="word"> Funny </tspan><tspan class="star">★</tspan><tspan class="word"> Sad</tspan></text>
      <text transform="translate(14,860) rotate(-90)" textLength="855" lengthAdjust="spacingAndGlyphs"><tspan class="word">Funny </tspan><tspan class="star">★</tspan><tspan class="word"> Sad </tspan><tspan class="star">★</tspan><tspan class="word"> Exciting </tspan><tspan class="star">★</tspan><tspan class="word"> Mysterious </tspan><tspan class="star">★</tspan><tspan class="word"> Fantastic </tspan><tspan class="star">★</tspan><tspan class="word"> Boring </tspan><tspan class="star">★</tspan><tspan class="word"> Enthralling </tspan><tspan class="star">★</tspan><tspan class="word"> Interesting </tspan><tspan class="star">★</tspan><tspan class="word"> Funny </tspan><tspan class="star">★</tspan><tspan class="word"> Sad </tspan><tspan class="star">★</tspan><tspan class="word"> Exciting</tspan></text>
      <text transform="translate(382,857) rotate(180)" textLength="372" lengthAdjust="spacingAndGlyphs"><tspan class="word">Fantastic </tspan><tspan class="star">★</tspan><tspan class="word"> Boring </tspan><tspan class="star">★</tspan><tspan class="word"> Enthralling </tspan><tspan class="star">★</tspan><tspan class="word"> Interesting</tspan></text>
    </svg>
    <div class="panel">
      <span class="school-mark" aria-hidden="true"></span>
      <h1 class="school-name">Marrowby Lane School</h1>
      <div class="kids-art" role="img" aria-label="Cartoon of two smiling children, one wearing a crown"></div>
      <h2 class="prompt">What did you think of<br>this book?</h2>
      <ul class="writing-lines" aria-label="Space for comments">
        <li></li><li></li><li></li><li></li><li></li><li></li><li></li>
        <li></li><li></li><li></li><li></li><li></li><li></li><li></li>
      </ul>
      <p class="pass-on">Pass it on!</p>
    </div>
  </article>

  <article class="bookmark bookmark--back">
    <svg class="border-words" viewBox="0 0 412 873" aria-hidden="true">
      <text x="40" y="16" textLength="365" lengthAdjust="spacingAndGlyphs"><tspan class="word">Funny </tspan><tspan class="star">★</tspan><tspan class="word"> Sad </tspan><tspan class="star">★</tspan><tspan class="word"> Exciting </tspan><tspan class="star">★</tspan><tspan class="word"> Mysterious </tspan><tspan class="star">★</tspan><tspan class="word"> Fantastic</tspan></text>
      <text transform="translate(398,40) rotate(90)" textLength="805" lengthAdjust="spacingAndGlyphs"><tspan class="word">Funny </tspan><tspan class="star">★</tspan><tspan class="word"> Sad </tspan><tspan class="star">★</tspan><tspan class="word"> Exciting </tspan><tspan class="star">★</tspan><tspan class="word"> Mysterious </tspan><tspan class="star">★</tspan><tspan class="word"> Fantastic </tspan><tspan class="star">★</tspan><tspan class="word"> Boring </tspan><tspan class="star">★</tspan><tspan class="word"> Enthralling </tspan><tspan class="star">★</tspan><tspan class="word"> Interesting </tspan><tspan class="star">★</tspan><tspan class="word"> Funny </tspan><tspan class="star">★</tspan><tspan class="word"> Sad</tspan></text>
      <text transform="translate(14,860) rotate(-90)" textLength="855" lengthAdjust="spacingAndGlyphs"><tspan class="word">Funny </tspan><tspan class="star">★</tspan><tspan class="word"> Sad </tspan><tspan class="star">★</tspan><tspan class="word"> Exciting </tspan><tspan class="star">★</tspan><tspan class="word"> Mysterious </tspan><tspan class="star">★</tspan><tspan class="word"> Fantastic </tspan><tspan class="star">★</tspan><tspan class="word"> Boring </tspan><tspan class="star">★</tspan><tspan class="word"> Enthralling </tspan><tspan class="star">★</tspan><tspan class="word"> Interesting </tspan><tspan class="star">★</tspan><tspan class="word"> Funny </tspan><tspan class="star">★</tspan><tspan class="word"> Sad </tspan><tspan class="star">★</tspan><tspan class="word"> Exciting</tspan></text>
      <text transform="translate(382,857) rotate(180)" textLength="372" lengthAdjust="spacingAndGlyphs"><tspan class="word">Fantastic </tspan><tspan class="star">★</tspan><tspan class="word"> Boring </tspan><tspan class="star">★</tspan><tspan class="word"> Enthralling </tspan><tspan class="star">★</tspan><tspan class="word"> Interesting</tspan></text>
    </svg>
    <div class="panel">
      <span class="school-mark" aria-hidden="true"></span>
      <h1 class="school-name">Marrowby Lane School</h1>
      <div class="kids-art" role="img" aria-label="Cartoon of two smiling children, one wearing a crown"></div>
      <h2 class="prompt">What did you think of<br>this book?</h2>
      <ul class="writing-lines" aria-label="Space for comments">
        <li></li><li></li><li></li><li></li><li></li><li></li><li></li>
        <li></li><li></li><li></li><li></li><li></li><li></li><li></li>
      </ul>
      <p class="pass-on">Pass it on!</p>
    </div>
  </article>

</main>
</body>
</html>
```